Mechanical Engineering Business needs a Label Design for Bottle.

We need a Label design for 2 Bottle Sizes of Milling Gel. This is used for Machine Work Shops big and small to do applications for different cutting processes. Example : Tapping / Broaching / Drilling / Reaming / Knurling / etc. An example of a similar product can be found at https://grivolex.com/product/16-oz-grivolex-bottle/ ... https://grivolex.com/product/2-oz-grivolex-bottle/ ... Our product will be named Mil - Gel or Milling - Gel with our Company logo attached. Currently, we are open to ideas and do not have any fixed concept.

```html
<!DOCTYPE html>
<html lang="en">
<head>
<meta charset="utf-8">
<title>Milling Gel Bottle Label</title>
<link rel="stylesheet" href="https://fonts.googleapis.com/css2?family=Anton&family=Oswald:wght@600&display=swap">
<style>
  :root {
    --page: #ffffff;
    --steel-light: #f4f5f6;
    --steel-mid: #c9ccd0;
    --steel-dark: #9a9ea4;
    --carbon-dark: #0e0f10;
    --carbon-mid: #2a2c2e;
    --brand-red: #8c1a33;
    --label-white: #ffffff;
    --rivet-rim: #7d8187;
    --rivet-core: #e9ebed;
    --band-edge: #5d6065;
    --ink: #1b1c1e;
  }
  * { margin: 0; padding: 0; box-sizing: border-box; }
  html, body {
    width: 1200px; height: 1200px; overflow: hidden;
    background: var(--page);
  }
  .label {
    position: absolute; left: 100px; top: 92px;
    width: 1000px; height: 1015px;
    box-shadow: 6px 10px 18px rgba(0,0,0,0.25);
    overflow: hidden;
  }
  .steel {
    position: absolute; left: 0; width: 100%;
    background:
      repeating-linear-gradient(0deg, rgba(255,255,255,0.18) 0 2px, rgba(0,0,0,0.04) 2px 4px),
      linear-gradient(100deg, var(--steel-dark) 0%, var(--steel-light) 22%, var(--steel-mid) 45%, var(--steel-light) 70%, var(--steel-dark) 100%);
  }
  .steel-top { top: 0; height: 356px; }
  .steel-bottom { top: 853px; height: 162px; }
  .brand {
    position: absolute; top: 196px; left: 0; width: 100%;
    display: flex; justify-content: center; align-items: center; gap: 14px;
    font-family: "Oswald", sans-serif; font-weight: 600;
    font-size: 40px; letter-spacing: 1px; color: var(--brand-red);
  }
  .brand-dot { width: 34px; height: 34px; border-radius: 50%; background: var(--brand-red); }
  .rivets {
    position: absolute; left: 0; width: 100%;
    display: flex; justify-content: space-around; padding: 0 60px;
  }
  .rivets-top { top: 296px; }
  .rivets-bottom { top: 893px; padding: 0 140px; }
  .rivet {
    width: 28px; height: 28px; border-radius: 50%;
    background: radial-gradient(circle at 45% 40%, var(--rivet-core) 0 30%, var(--rivet-rim) 60%, #4b4e52 100%);
    box-shadow: inset 0 1px 2px rgba(0,0,0,0.5);
  }
  .carbon {
    position: absolute; top: 356px; left: 0; width: 100%; height: 497px;
    background: radial-gradient(ellipse at 50% 45%, var(--carbon-mid) 0%, var(--carbon-dark) 80%);
    border-top: 6px solid var(--band-edge); border-bottom: 6px solid var(--band-edge);
  }
  .product-name {
    position: absolute; top: 356px; left: 0; width: 100%; height: 497px;
    display: flex; flex-direction: column; justify-content: center; align-items: center;
    font-family: "Anton", sans-serif; font-weight: 400; color: var(--label-white);
    font-size: 170px; line-height: 1.0; text-transform: uppercase;
    text-shadow: 4px 6px 8px rgba(0,0,0,0.8);
  }
  .part-number {
    position: absolute; top: 955px; left: 0; width: 100%;
    text-align: center; font-family: "Oswald", sans-serif; font-weight: 600;
    font-size: 24px; color: var(--ink);
  }
</style>
</head>
<body>
  <div class="label">
    <div class="steel steel-top"></div>
    <div class="brand"><span class="brand-dot"></span><span class="brand-name">VARNELL TOOLS</span></div>
    <div class="rivets rivets-top">
      <span class="rivet"></span><span class="rivet"></span><span class="rivet"></span><span class="rivet"></span><span class="rivet"></span>
    </div>
    <div class="carbon" role="img" aria-label="Dark hexagonal carbon mesh texture band"></div>
    <h1 class="product-name"><span>Milling</span><span>Gel</span></h1>
    <div class="steel steel-bottom"></div>
    <div class="rivets rivets-bottom">
      <span class="rivet"></span><span class="rivet"></span><span class="rivet"></span><span class="rivet"></span><span class="rivet"></span>
    </div>
    <p class="part-number">Part No 7318 · 4 oz (120 ml)</p>
  </div>
</body>
</html>
```